KTR Engineering Pty Ltd

I have already had Corvale welding and fabrication cards made , my business has changed too KTR engineering Pty Ltd so I need my logo changed on the cards
one side have my logo then the other side have what we do.
front side logo and details
owner /operator : Lachlan Meravic
email: ktr.works@ironvalemail.com
number: 0491537204
ABN: 47 261 538 902
ACN: 718 352 946
on back have in dot points what we do:
* structural steel erection
* precast panels
* site welding
*steel alteration & repair
* rigging & dogging
*labour hire
all details in breif

```html
<!DOCTYPE html>
<html lang="en">
<head>
<meta charset="utf-8">
<title>KTR Engineering Pty Ltd — Business Cards</title>
<link href="https://fonts.googleapis.com/css2?family=Mulish:wght@400;600;800&display=swap" rel="stylesheet">
<style>
  :root {
    --backdrop: #7e9aba;
    --card-white: #ffffff;
    --rust: #9b4c3d;
    --rust-light: #a85a49;
    --navy: #2a3342;
    --ink: #1f2530;
    --paper-text: #ffffff;
  }
  * { box-sizing: border-box; margin: 0; padding: 0; }
  html, body {
    width: 1200px; height: 876px; overflow: hidden;
    background: var(--backdrop);
    font-family: "Mulish", Arial, sans-serif;
  }
  .canvas {
    position: relative; width: 1200px; height: 876px;
    display: flex; align-items: center; justify-content: center; gap: 44px;
  }
  .card {
    width: 524px; height: 320px; position: relative;
    box-shadow: 0 10px 24px rgba(30, 45, 70, 0.35);
  }

  /* Back: services */
  .card--back {
    background: linear-gradient(135deg, var(--rust-light), var(--rust));
    color: var(--paper-text);
    display: flex; flex-direction: column; align-items: center; justify-content: center;
  }
  .brand-name {
    font-weight: 800; letter-spacing: 0.02em; text-transform: uppercase; line-height: 1.05;
    display: flex; align-items: center; gap: 12px;
  }
  .brand-mark { width: 14px; height: 14px; border-radius: 50%; flex: none; }
  .card--back .brand-name { font-size: 34px; color: var(--paper-text); text-align: center; }
  .card--back .brand-mark { background: var(--paper-text); }
  .services {
    list-style: none; margin-top: 40px;
    display: grid; grid-template-columns: auto auto auto; column-gap: 22px; row-gap: 8px;
    font-size: 15px; font-weight: 600;
  }
  .services li::before { content: "• "; }

  /* Front: logo and details */
  .card--front {
    background: var(--card-white);
    display: flex; align-items: center; padding: 0 30px;
  }
  .card--front .brand-name {
    font-size: 22px; color: var(--navy); width: 190px;
  }
  .card--front .brand-mark { background: var(--rust); }
  .divider { width: 2px; height: 150px; background: var(--rust); margin: 0 22px; flex: none; }
  .contact { color: var(--ink); font-size: 14px; line-height: 1.45; }
  .contact__name { font-size: 21px; font-weight: 800; letter-spacing: 0.06em; }
  .contact__role { font-size: 14px; margin-bottom: 4px; }
  .contact__line { display: flex; align-items: center; gap: 6px; }
  .contact__icon { width: 16px; height: 16px; flex: none; }
  .label { color: var(--rust); font-weight: 800; }
</style>
</head>
<body>
<main class="canvas">
  <section class="card card--back" aria-label="Card back: services">
    <div class="brand-name"><span class="brand-mark"></span>KTR Engineering<br>Pty Ltd</div>
    <ul class="services">
      <li>Structural steel erection</li>
      <li>Precast panels</li>
      <li>Site welding</li>
      <li>Steel alteration &amp; repair</li>
      <li>Rigging &amp; dogging</li>
      <li>Labour hire</li>
    </ul>
  </section>

  <section class="card card--front" aria-label="Card front: contact details">
    <div class="brand-name"><span class="brand-mark"></span>KTR Engineering Pty Ltd</div>
    <div class="divider"></div>
    <div class="contact">
      <p class="contact__name">Lachlan Meravic</p>
      <p class="contact__role">Owner/Operator</p>
      <p class="contact__line">
        <svg class="contact__icon" viewBox="0 0 16 16" aria-hidden="true">
          <rect width="16" height="16" rx="3" fill="#9b4c3d"/>
          <path d="M5 3.5l2 2-1 1.2c.6 1.3 1.6 2.3 2.9 2.9l1.2-1 2 2-1.2 1.4C8 11.8 4.2 8 3.6 4.7z" fill="#fff"/>
        </svg>
        0491537204
      </p>
      <p class="contact__line">
        <svg class="contact__icon" viewBox="0 0 16 16" aria-hidden="true">
          <rect width="16" height="16" rx="3" fill="#9b4c3d"/>
          <rect x="3" y="4.5" width="10" height="7" fill="none" stroke="#fff" stroke-width="1.2"/>
          <path d="M3 4.5l5 4 5-4" fill="none" stroke="#fff" stroke-width="1.2"/>
        </svg>
        ktr.works@ironvalemail.com
      </p>
      <p><span class="label">ABN:</span> 47 261 538 902</p>
      <p><span class="label">ACN:</span> 718 352 946</p>
    </div>
  </section>
</main>
</body>
</html>
```